A start up special flyer design!

Hi All - Have updated the attachment content - This is the info required for the designs.
I need a catchy flyer to send out to a few areas to advertise the start of my plumbing business!
The flyer will contain an offer for customers, which will need to have some key details on it. See attached. Feel free to fit these criteria into the flyer given your knowledge on design and messaging principles. Key thing to get across to customers is the discount and special offer, and that it is a start up offer.
I have a logo that needs to be on the flyer as well - let me know what format you require and I will send through to you.
The color scheme needs to be blue / grey / black / white.
Let me know if you have any questions.
I

```html
<!DOCTYPE html>
<html lang="en">
<head>
<meta charset="utf-8">
<title>Harbour Line Plumbing – Start-up Offer Flyer</title>
<link rel="stylesheet" href="https://fonts.googleapis.com/css2?family=PT+Sans:wght@400;700&family=PT+Sans+Narrow:wght@400;700&display=swap">
<style>
  :root {
    --navy: #1d4a85;
    --navy-deep: #143a6b;
    --blue: #2a78bd;
    --cyan: #3cb4e3;
    --cyan-light: #7fd0ef;
    --paper: #f2f2f2;
    --white: #ffffff;
    --grey: #6b6b6b;
    --grey-line: #a9a9a9;
    --backdrop: #e6e8eb;
  }
  * { margin: 0; padding: 0; box-sizing: border-box; }
  html, body {
    width: 1124px; height: 1200px; overflow: hidden;
    background: var(--backdrop);
  }
  .canvas { position: relative; width: 1124px; height: 1200px; }
  .flyer {
    position: absolute; left: 110px; top: 20px;
    width: 877px; height: 1125px;
    transform: scale(1.031); transform-origin: top left;
    background: var(--paper);
    overflow: hidden;
    font-family: "PT Sans", sans-serif;
    box-shadow: 0 4px 18px rgba(0,0,0,0.18);
  }
  .flyer-shapes { position: absolute; inset: 0; }

  .brand {
    position: absolute; left: 20px; top: 60px; width: 300px;
    text-align: center; color: var(--navy);
    font-family: "PT Sans", sans-serif; font-weight: 700;
  }
  .brand-dot {
    display: block; width: 34px; height: 34px; margin: 0 auto 10px;
    border-radius: 50%; background: var(--navy);
  }
  .brand-name { font-size: 30px; line-height: 1.05; letter-spacing: 1px; }
  .brand-sub { font-size: 17px; letter-spacing: 9px; margin-top: 4px; }

  .tagline {
    position: absolute; left: 398px; top: 0; width: 465px; height: 103px;
    display: flex; align-items: center; justify-content: center;
    color: var(--white);
    font-family: "PT Sans Narrow", sans-serif; font-weight: 700;
    font-size: 35px; white-space: nowrap;
  }

  .offer {
    position: absolute; left: 33px; width: 352px; height: 137px;
    background: var(--white);
    border: 1.5px dashed var(--grey-line);
    text-align: center;
    color: var(--navy);
    font-family: "PT Sans Narrow", sans-serif; font-weight: 700;
    box-shadow: 0 9px 6px -6px rgba(0,0,0,0.25);
    display: flex; flex-direction: column; justify-content: center;
  }
  .offer--discount { top: 287px; }
  .offer--gst { top: 446px; }
  .offer--hotwater { top: 610px; }
  .offer-headline { font-size: 31px; line-height: 1.12; white-space: nowrap; }
  .offer-big { font-size: 56px; line-height: 1; letter-spacing: -2px; }
  .offer-rest { font-size: 26px; }
  .offer-note {
    font-family: "PT Sans", sans-serif; font-weight: 400;
    font-size: 13px; color: var(--grey); margin-top: 8px; white-space: nowrap;
  }

  .services {
    position: absolute; left: 0; top: 815px; width: 877px;
    text-align: center; color: var(--navy);
    font-family: "PT Sans Narrow", sans-serif; font-weight: 700;
    font-size: 38px; line-height: 54px; white-space: nowrap;
  }

  .booking {
    position: absolute; right: 14px; top: 958px; width: 440px;
    text-align: right; color: var(--white);
    font-size: 20px; line-height: 28px;
  }

  .contact { position: absolute; left: 32px; top: 990px; list-style: none; }
  .contact-item {
    display: flex; align-items: center; height: 40px;
    color: var(--white);
    font-family: "PT Sans Narrow", sans-serif; font-weight: 700; font-size: 27px;
    white-space: nowrap;
  }
  .contact-icon { width: 24px; height: 24px; margin-right: 15px; flex: none; }
</style>
</head>
<body>
<div class="canvas">
  <div class="flyer">
    <svg class="flyer-shapes" width="877" height="1125" viewBox="0 0 877 1125" xmlns="http://www.w3.org/2000/svg">
      <defs>
        <linearGradient id="topWave" x1="0" y1="0" x2="1" y2="0">
          <stop offset="0" stop-color="#7fd0ef"/>
          <stop offset="1" stop-color="#1fa6df"/>
        </linearGradient>
        <linearGradient id="band" x1="0" y1="0" x2="1" y2="0">
          <stop offset="0" stop-color="#1d4a85"/>
          <stop offset="1" stop-color="#2a78bd"/>
        </linearGradient>
        <linearGradient id="footer" x1="0" y1="0" x2="1" y2="0">
          <stop offset="0" stop-color="#143a6b"/>
          <stop offset="1" stop-color="#2a78bd"/>
        </linearGradient>
        <linearGradient id="footerWave" x1="0" y1="0" x2="1" y2="0">
          <stop offset="0" stop-color="#8fd6f2"/>
          <stop offset="1" stop-color="#12a0dc"/>
        </linearGradient>
        <radialGradient id="logoDisc" cx="0.5" cy="0.4" r="0.6">
          <stop offset="0.6" stop-color="#ffffff"/>
          <stop offset="1" stop-color="#e4e4e4"/>
        </radialGradient>
        <linearGradient id="photoMain" x1="0" y1="0" x2="1" y2="1">
          <stop offset="0" stop-color="#e9eef3"/>
          <stop offset="0.5" stop-color="#9fb4cc"/>
          <stop offset="1" stop-color="#3d66a3"/>
        </linearGradient>
        <radialGradient id="photoDrain" cx="0.5" cy="0.5" r="0.6">
          <stop offset="0" stop-color="#2b5f9a"/>
          <stop offset="1" stop-color="#cfe3f2"/>
        </radialGradient>
        <linearGradient id="photoPipes" x1="0" y1="0" x2="1" y2="1">
          <stop offset="0" stop-color="#dfe6ec"/>
          <stop offset="1" stop-color="#6d8fb8"/>
        </linearGradient>
      </defs>

      <!-- header waves -->
      <path d="M0 0 H877 V130 C760 135 640 150 520 190 C380 235 200 255 0 250 Z" fill="url(#topWave)"/>
      <path d="M0 232 C200 238 380 215 520 172 C640 135 760 125 877 120" fill="none" stroke="#ffffff" stroke-width="4"/>
      <rect x="380" y="0" width="497" height="103" fill="url(#band)"/>
      <ellipse cx="175" cy="45" rx="210" ry="178" fill="url(#logoDisc)"/>

      <!-- photo circles -->
      <g role="img" aria-label="Photo: plumber in blue cap and shirt fixing the waste pipe under a sink with a wrench">
        <circle cx="649" cy="402" r="247" fill="url(#photoMain)" stroke="#5ec2ea" stroke-width="6"/>
      </g>
      <g role="img" aria-label="Photo: close-up of a sink drain with running water">
        <circle cx="546" cy="662" r="82" fill="url(#photoDrain)" stroke="#3cb4e3" stroke-width="5"/>
      </g>
      <g role="img" aria-label="Photo: gloved hands fitting a pipe valve">
        <circle cx="758" cy="715" r="90" fill="url(#photoPipes)" stroke="#3cb4e3" stroke-width="5"/>
      </g>

      <!-- footer waves -->
      <path d="M0 918 C170 900 300 945 420 1000 C540 1055 700 1075 877 1060 V1125 H0 Z" fill="url(#footer)"/>
      <path d="M340 990 C480 935 680 905 877 915 V1060 C700 1100 520 1070 340 990 Z" fill="url(#footerWave)"/>
      <path d="M345 992 C520 1068 700 1098 877 1062" fill="none" stroke="#ffffff" stroke-width="4"/>
    </svg>

    <div class="brand">
      <span class="brand-dot"></span>
      <div class="brand-name">HARBOUR LINE</div>
      <div class="brand-sub">PLUMBING</div>
    </div>

    <div class="tagline">QUALITY WORK AT A DECENT PRICE</div>

    <section class="offer offer--discount">
      <div class="offer-headline"><span class="offer-big">15% OFF</span> <span class="offer-rest">your overall bill</span></div>
      <div class="offer-note">Offer valid between 15 August 2016 to 15 October 2016.</div>
    </section>
    <section class="offer offer--gst">
      <div class="offer-headline">No GST payable, saving you<br>additional 10% on your bill</div>
      <div class="offer-note">Offer valid until 30 September 2016.</div>
    </section>
    <section class="offer offer--hotwater">
      <div class="offer-headline">Plus, a free hot water health<br>check and replacement quote</div>
      <div class="offer-note">Quote valid for 12 months from the quote date.</div>
    </section>

    <div class="services">ALL PLUMBING, DRAINING, AND GASFITTING WORKS<br>LOCAL PLUMBER</div>

    <p class="booking">To make an appointment,<br>call or email Marcus, or alternatively make a<br>booking directly on the website</p>

    <ul class="contact">
      <li class="contact-item">
        <svg class="contact-icon" viewBox="0 0 24 24"><circle cx="12" cy="12" r="12" fill="#fff"/><path d="M8.2 6.5c.5-.3 1.1-.2 1.4.3l1 1.8c.3.5.1 1-.3 1.3l-.7.5c.6 1.4 1.6 2.5 3 3.1l.5-.7c.3-.4.9-.6 1.3-.3l1.8 1c.5.3.6.9.3 1.4l-.7 1c-.5.6-1.3.9-2 .6-3.3-1.2-5.8-3.7-7-7-.3-.8 0-1.6.6-2.1z" fill="#143a6b"/></svg>
        0400 512 688
      </li>
      <li class="contact-item">
        <svg class="contact-icon" viewBox="0 0 24 24"><circle cx="12" cy="12" r="12" fill="#fff"/><rect x="6" y="8" width="12" height="8.5" rx="1" fill="#143a6b"/><path d="M6.5 8.6 12 13l5.5-4.4" fill="none" stroke="#fff" stroke-width="1.3"/></svg>
        marcus@harbourlineplumbing.com
      </li>
      <li class="contact-item">
        <svg class="contact-icon" viewBox="0 0 24 24"><circle cx="12" cy="12" r="12" fill="#fff"/><g fill="none" stroke="#143a6b" stroke-width="1.4"><circle cx="12" cy="12" r="7"/><ellipse cx="12" cy="12" rx="3" ry="7"/><path d="M5 12h14M6 8.5h12M6 15.5h12"/></g></svg>
        www.harbourlineplumbing.com
      </li>
    </ul>
  </div>
</div>
</body>
</html>
```